Venture Backed Startup Company for SaaS Lead Generation ***Guaranteed Payment and Fast Feedback***

***Guaranteed Payment***
***I Give Fast Feedback***

I need a one-page website design for a startup company. We sell lead generation and appointment setting services to B2B SaaS companies.

Looking for a clean, modern, flat, "Saas-style" design. A simple but trustworthy and authoritative color palette is best. Pictures of actual people are very good to use too

Here are some websites I like and the reasons why:

https://www.pellarin.com - simple and intuitive design, very clear, strong CTA, explains the process succinctly, and has pics of people/faces\

https://www.tovemark.com/ - clean and simple, flat design, strong CTA, easy to understand

https://www.quorvel.io/ - simple and clean navigation, easy to understand what to do next

https://brisketfolder.com/ - strong step by step approach, easy to understand the value of the website, clean and sharp design

https://pinwardle.com/ - Great color scheme, clean, easy to read, great font

Target Market(s)

startups, entrepeneur, B2B SaaS

Industry/Entity Type

SaaS

Number of Pages Required

1 page

Font styles to use
Sans Serif

Colors

Designer to choose colors to be used in the design.

Requirements
Must have
• Good graphics, a theme, and pictures of people
Nice to have
• Here are other websites like and the reason why
• https://marqueloft.com/ - Great graphics, clean and flat design, pictures of people, modern design
• https://dunvelio.com/ - Clean, pictures of people, easy to read, good contrast
• https://yarrowpeak.co/ -- Good graphics and great font, easy to read, great color scheme
• http://tillerandvane.com/ - clean design

```html
<!DOCTYPE html>
<html lang="en">
<head>
<meta charset="utf-8">
<title>Lead Generation &amp; Appointment Setting for B2B SaaS</title>
<link href="https://fonts.googleapis.com/css2?family=Montserrat:ital,wght@0,400;0,500;0,600;0,700;1,500&display=swap" rel="stylesheet">
<style>
  :root {
    --blue: #1f6fd8;
    --blue-deep: #1a5fe0;
    --blue-bright: #3aa0ff;
    --blue-pale: #f2f6fc;
    --orange: #f7931e;
    --orange-deep: #ff5e1a;
    --text: #2c3440;
    --muted: #4a5360;
    --white: #ffffff;
    --border: #dfe3ea;
  }
  * { margin: 0; padding: 0; box-sizing: border-box; }
  html, body { width: 1200px; height: 2553px; overflow: hidden; background: var(--white); }
  body { font-family: "Montserrat", Arial, sans-serif; color: var(--text); }
  .page { position: relative; width: 1200px; height: 2553px; overflow: hidden; }
  .abs { position: absolute; }

  .deco { position: absolute; }
  .btn {
    position: absolute; display: flex; align-items: center; justify-content: center;
    color: var(--white); font-weight: 600; font-size: 13px; text-decoration: none;
    border-radius: 22px;
    background: linear-gradient(90deg, var(--orange), var(--orange-deep));
    box-shadow: 0 8px 18px rgba(255, 110, 30, .3);
  }

  /* header */
  .logo { left: 150px; top: 42px; font-size: 25px; font-weight: 700; color: var(--white); letter-spacing: 2px; }
  .nav a { position: absolute; top: 48px; font-size: 13px; font-weight: 500; color: var(--blue); text-decoration: none; }
  .nav a.active::after { content: ""; position: absolute; left: 0; right: 0; top: 31px; height: 1px; background: var(--blue); }

  /* hero */
  .hero-title { left: 150px; top: 226px; font-size: 34px; line-height: 45px; font-weight: 700; color: var(--blue); }
  .hero-art { left: 664px; top: 150px; width: 536px; height: 640px; }

  /* about */
  .section-title { font-size: 25px; font-weight: 700; color: var(--blue); }
  .about-text { left: 150px; top: 678px; width: 470px; font-size: 13px; line-height: 25px; color: var(--muted); }
  .checklist { left: 150px; top: 810px; list-style: none; }
  .checklist li { display: flex; align-items: center; height: 36px; font-size: 13px; color: var(--muted); }
  .checklist svg { margin-right: 22px; }

  .partners-label { left: 764px; top: 647px; font-size: 14px; font-weight: 600; letter-spacing: 3px; color: var(--blue); }
  .partner {
    position: absolute; left: 757px; width: 162px; height: 62px;
    border: 1px solid var(--border); background: var(--white);
    display: flex; align-items: center; justify-content: center;
    box-shadow: 0 4px 12px rgba(30, 60, 120, .06);
  }
  .partner span { display: block; width: 80px; height: 18px; border-radius: 9px; background: #c9ced6; }

  /* features */
  .center { left: 0; width: 1200px; text-align: center; }
  .lede { font-size: 13px; line-height: 24px; color: var(--muted); }
  .feature { position: absolute; width: 320px; text-align: center; }
  .feature-icon { margin: 0 auto; width: 140px; height: 136px; position: relative; }
  .feature-icon .glyph {
    position: absolute; left: 40px; top: 38px; width: 60px; height: 60px; border-radius: 14px;
    background: linear-gradient(150deg, #cfe2fb, #7fb0ef);
    opacity: .8;
  }
  .feature h3 { margin-top: 44px; font-size: 15px; font-weight: 600; color: var(--blue); }
  .feature p { margin-top: 14px; font-size: 12.5px; line-height: 24px; color: var(--muted); }

  /* testimonials */
  .avatar { left: 530px; top: 1820px; width: 150px; height: 150px; }
  .avatar-photo {
    position: absolute; left: 10px; top: 0; width: 140px; height: 140px;
    background: linear-gradient(160deg, #d9dde2, #8f99a6);
    clip-path: polygon(25% 4%, 75% 4%, 100% 50%, 75% 96%, 25% 96%, 0 50%);
  }
  .client-name { top: 1982px; font-size: 14px; font-style: italic; font-weight: 500; color: var(--blue); }
  .quote-mark { left: 364px; top: 2000px; font-size: 40px; font-weight: 700; color: var(--blue); line-height: 1; }
  .quote { left: 400px; top: 2018px; width: 435px; font-size: 12.5px; line-height: 24px; color: var(--muted); }
  .arrow {
    position: absolute; top: 1952px; width: 34px; height: 34px; border-radius: 50%;
    background: linear-gradient(135deg, var(--orange), var(--orange-deep));
    box-shadow: 0 6px 14px rgba(255, 110, 30, .35);
    display: flex; align-items: center; justify-content: center;
  }
  .dots { top: 2156px; display: flex; justify-content: center; gap: 9px; }
  .dots i { width: 8px; height: 8px; border-radius: 50%; background: var(--orange-deep); }
  .dots i.dim { background: #f9a98a; }
</style>
</head>
<body>
<div class="page">

  <!-- decorative shapes -->
  <svg class="deco" style="left:0;top:0" width="420" height="130" viewBox="0 0 420 130" aria-hidden="true">
    <defs><linearGradient id="topBand" x1="0" y1="0" x2="1" y2="1"><stop offset="0" stop-color="#1a5fe0"/><stop offset="1" stop-color="#3aa0ff"/></linearGradient></defs>
    <polygon points="0,0 408,0 200,123 160,123 0,35" fill="url(#topBand)"/>
  </svg>
  <svg class="deco" style="left:350px;top:95px" width="130" height="90" aria-hidden="true"><polygon points="20,45 65,10 120,40 75,80" fill="#f2f6fc"/></svg>
  <svg class="deco" style="left:25px;top:495px" width="100" height="60" aria-hidden="true"><polygon points="5,30 40,5 95,25 55,55" fill="#f2f6fc"/></svg>
  <svg class="deco" style="left:0;top:1010px" width="110" height="140" aria-hidden="true"><polygon points="0,10 100,70 0,130" fill="#f2f6fc"/></svg>
  <svg class="deco" style="left:1050px;top:1055px" width="150" height="90" aria-hidden="true"><polygon points="10,45 70,8 140,35 80,80" fill="#f2f6fc"/></svg>
  <svg class="deco" style="left:1010px;top:1160px" width="100" height="60" aria-hidden="true"><polygon points="5,30 45,5 95,25 55,55" fill="#f2f6fc"/></svg>
  <svg class="deco" style="left:20px;top:1770px" width="160" height="110" aria-hidden="true"><polygon points="10,40 45,15 85,30 50,55" fill="#f2f6fc"/><polygon points="30,80 85,45 150,70 95,105" fill="#f2f6fc"/></svg>
  <svg class="deco" style="left:1085px;top:2120px" width="115" height="80" aria-hidden="true"><polygon points="5,40 55,8 115,30 65,75" fill="#f4f6fa"/></svg>
  <svg class="deco" style="left:1055px;top:1642px" width="145" height="222" aria-hidden="true">
    <defs><linearGradient id="rightTri" x1="0" y1="0" x2="1" y2="1"><stop offset="0" stop-color="#3aa0ff"/><stop offset="1" stop-color="#1a5fe0"/></linearGradient></defs>
    <polygon points="145,0 145,222 0,100" fill="url(#rightTri)"/>
  </svg>
  <svg class="deco" style="left:0;top:2093px" width="180" height="230" aria-hidden="true">
    <defs><linearGradient id="leftTri" x1="0" y1="0" x2="1" y2="1"><stop offset="0" stop-color="#1a5fe0"/><stop offset="1" stop-color="#3aa0ff"/></linearGradient></defs>
    <polygon points="0,0 179,122 0,230" fill="url(#leftTri)"/>
  </svg>

  <!-- header -->
  <div class="abs logo">LOGO</div>
  <nav class="nav">
    <a class="active" href="#about" style="left:543px">About Us</a>
    <a href="#features" style="left:650px">Features</a>
    <a href="#testimonials" style="left:754px">Testimonials</a>
    <a href="#pricing" style="left:883px">Pricing</a>
  </nav>
  <a class="btn" href="#signup" style="left:972px;top:37px;width:106px;height:40px">Sign Up</a>

  <!-- hero -->
  <h1 class="abs hero-title">Lead Generation &amp;<br>Appointment Setting Services<br>for B2B SaaS Companies</h1>
  <a class="btn" href="#about" style="left:151px;top:402px;width:135px;height:40px">Learn More</a>
  <svg class="abs hero-art" viewBox="0 0 536 640" role="img" aria-label="Isometric illustration of a laptop with a launching rocket, charts and clouds">
    <defs>
      <linearGradient id="heroPlane" x1="0" y1="0" x2="1" y2="1">
        <stop offset="0" stop-color="#3aa0ff"/><stop offset="1" stop-color="#1a5fe0"/>
      </linearGradient>
      <radialGradient id="heroGlow" cx="0.5" cy="0.5" r="0.5">
        <stop offset="0" stop-color="#ffffff" stop-opacity=".55"/><stop offset="1" stop-color="#ffffff" stop-opacity="0"/>
      </radialGradient>
    </defs>
    <polygon points="20,300 300,110 536,260 536,640" fill="#f2f6fc"/>
    <polygon points="0,258 290,30 536,150 536,515" fill="url(#heroPlane)"/>
    <ellipse cx="300" cy="200" rx="200" ry="130" fill="url(#heroGlow)"/>
  </svg>

  <!-- about -->
  <h2 class="abs section-title" id="about" style="left:150px;top:601px">About Us</h2>
  <p class="abs about-text">We create modern IT solutions to increase lead generation and provide appointment setting services to B2B SaaS companies. Aliquam posuere augue vitae metu feugiat pellentesque. Pellentesque habiant morbitus tristique senectus et netus et malesuada fames ac turpis egestas.</p>
  <ul class="abs checklist">
    <li><svg width="14" height="14" viewBox="0 0 14 14"><circle cx="7" cy="7" r="7" fill="#f7931e"/><path d="M4 7.2l2 2 4-4.4" stroke="#fff" stroke-width="1.8" fill="none" stroke-linecap="round"/></svg>Find new prospects</li>
    <li><svg width="14" height="14" viewBox="0 0 14 14"><circle cx="7" cy="7" r="7" fill="#f7931e"/><path d="M4 7.2l2 2 4-4.4" stroke="#fff" stroke-width="1.8" fill="none" stroke-linecap="round"/></svg>Get full profile information with verified emails</li>
    <li><svg width="14" height="14" viewBox="0 0 14 14"><circle cx="7" cy="7" r="7" fill="#f7931e"/><path d="M4 7.2l2 2 4-4.4" stroke="#fff" stroke-width="1.8" fill="none" stroke-linecap="round"/></svg>Use your network to reach more prospects</li>
    <li><svg width="14" height="14" viewBox="0 0 14 14"><circle cx="7" cy="7" r="7" fill="#f7931e"/><path d="M4 7.2l2 2 4-4.4" stroke="#fff" stroke-width="1.8" fill="none" stroke-linecap="round"/></svg>Gain access to more accounts through team network</li>
    <li><svg width="14" height="14" viewBox="0 0 14 14"><circle cx="7" cy="7" r="7" fill="#f7931e"/><path d="M4 7.2l2 2 4-4.4" stroke="#fff" stroke-width="1.8" fill="none" stroke-linecap="round"/></svg>Enrich your marketing data</li>
    <li><svg width="14" height="14" viewBox="0 0 14 14"><circle cx="7" cy="7" r="7" fill="#f7931e"/><path d="M4 7.2l2 2 4-4.4" stroke="#fff" stroke-width="1.8" fill="none" stroke-linecap="round"/></svg>95% email accuracy guarantee</li>
  </ul>

  <div class="abs partners-label">OUR PARTNERS</div>
  <div class="partner" style="top:684px"><span></span></div>
  <div class="partner" style="top:754px"><span></span></div>
  <div class="partner" style="top:824px"><span></span></div>
  <div class="partner" style="top:894px"><span></span></div>
  <div class="partner" style="top:963px"><span></span></div>

  <!-- features -->
  <h2 class="abs section-title center" id="features" style="top:1153px">Our Key Features</h2>
  <p class="abs lede center" style="top:1198px">Here are the best features that makes us the most<br>powerful, fast and user-friendly platform.</p>

  <div class="feature" style="left:114px;top:1302px">
    <div class="feature-icon">
      <svg width="140" height="136" aria-hidden="true"><polygon points="35,4 105,4 140,68 105,132 35,132 0,68" fill="#f2f6fc"/></svg>
      <div class="glyph" role="img" aria-label="Icon of a cloud with gears"></div>
    </div>
    <h3>Cloud Based Services</h3>
    <p>Nam in est quis lectus viverra blandit.<br>Curabitur quam sem, imperdiet nec<br>auctor quis, vehicula non est.</p>
  </div>
  <div class="feature" style="left:439px;top:1302px">
    <div class="feature-icon">
      <svg width="140" height="136" aria-hidden="true"><polygon points="35,4 105,4 140,68 105,132 35,132 0,68" fill="#f2f6fc"/></svg>
      <div class="glyph" role="img" aria-label="Icon of a safe with a cloud"></div>
    </div>
    <h3>Data Safe Solutions</h3>
    <p>Ut lorem magna, accumsan at tellus sit<br>amet, dignissim vulputate risus. Class<br>aptent taciti sociosqu ad litora torquen.</p>
  </div>
  <div class="feature" style="left:764px;top:1302px">
    <div class="feature-icon">
      <svg width="140" height="136" aria-hidden="true"><polygon points="35,4 105,4 140,68 105,132 35,132 0,68" fill="#f2f6fc"/></svg>
      <div class="glyph" role="img" aria-label="Icon of server storage with clouds"></div>
    </div>
    <h3>Fast &amp; Reliable Storage</h3>
    <p>Porttitor mollis quam quis aliquam. Fusce<br>varius massa vitae mauris vehicula, ac<br>dictum ipsum auctor.</p>
  </div>

  <!-- testimonials -->
  <h2 class="abs section-title center" id="testimonials" style="top:1724px">Our Customers Testimonials</h2>
  <div class="abs avatar">
    <svg class="abs" style="left:0;top:8px" width="150" height="142" aria-hidden="true"><polygon points="30,10 110,10 145,72 110,134 30,134 0,72" fill="none" stroke="#8fbaf2" stroke-width="6"/></svg>
    <div class="avatar-photo" role="img" aria-label="Portrait photo of the client"></div>
  </div>
  <div class="abs client-name center">Owen Marsh</div>
  <div class="abs quote-mark">&ldquo;</div>
  <p class="abs quote">Quisque consectetur commodo pellentesque. Maecenas sit amet egestas un lectus. Morbi sed dui consectetur, suscipit quam atnas, interdum nibh. Curabien mollis, tellus in ultricies ullamcorper terd, magn ibh placerat odio, vel ullamper.</p>
  <a class="arrow" href="#prev" style="left:243px" aria-label="Previous"><svg width="10" height="12"><path d="M7 1L2 6l5 5" stroke="#fff" stroke-width="2" fill="none"/></svg></a>
  <a class="arrow" href="#next" style="left:922px" aria-label="Next"><svg width="10" height="12"><path d="M3 1l5 5-5 5" stroke="#fff" stroke-width="2" fill="none"/></svg></a>
  <div class="abs dots center"><i></i><i class="dim"></i><i></i><i></i><i></i></div>
  <a class="btn" href="#signup" style="left:534px;top:2241px;width:135px;height:40px">Get Started</a>

  <!-- pricing -->
  <h2 class="abs section-title center" id="pricing" style="top:2425px">Pricing Plans</h2>
</div>
</body>
</html>
```